FREE BBQ for life if you win our business with your creative menu design

Looking for a 11x17 size menu. we are a full service BBQ restaurant. We have an upscale environment as well as up scale service. We offer 5 star dinning at a casual price. we are on route 66 and are proud of that. we offer the finest smoked meats. Specializing in smoked pork beef and bison. we have an old barn wood decor. we only use oak to smoke our meats. use a lot of tarnished metal as well as some string nail art. Looking for a menu that goes along our style. i have attached as many pictures as i could to give you a fill of how we do it out here.
PLEASE USE THE 11"X17" MENU TEMPLATE ATTACHED IN THE PROJECT BRIEF.
Target Market(s)
Cool people and there families.
Industry/Entity Type
Business
Requirements
Must have
- I have attached the Current menu we use. File pollards menu pub. Those are all the Items. There will be some changes as we but together the new menu. The prices are changing. but that should be an easy change as we go.
Nice to have
- We are getting away from the lunch dinner menu and going to an all day menu. so rather than coming with toast or bun we will now be asking as an option. I have attached a menu i tried to make as a sample of how we will be doing it. new menu single page and new menu single page flame. These are ideas i had but could not really make it work. so use them as an idea of what we are looking for but be creative.

```html
<!DOCTYPE html>
<html lang="en">
<head>
<meta charset="utf-8">
<title>Pollards Barbeque Menu</title>
<link rel="stylesheet" href="https://fonts.googleapis.com/css2?family=Alfa+Slab+One&family=Arimo:wght@400;700&display=swap">
<style>
:root{
  --bg:#d9d9d9;
  --ink:#161616;
  --red:#e5261b;
  --blue:#1f4fa8;
  --parchment-light:#f6e8c4;
  --parchment-mid:#ecd59f;
  --parchment-edge:#d7b574;
  --plank:#5b3b22;
  --plank-dark:#3a2414;
  --flame-dark:#1a0d06;
  --flame:#b2460f;
  --logo-orange:#f39a2b;
  --logo-navy:#1e2a66;
}
*{box-sizing:border-box;margin:0;padding:0}
html,body{width:869px;height:1200px;overflow:hidden;background:var(--bg)}
.menu{
  position:absolute;left:61px;top:26px;width:830px;height:1275px;
  transform:scale(.9);transform-origin:0 0;
  font-family:"Arimo",Arial,sans-serif;color:var(--ink);
  background:radial-gradient(ellipse at 10% 60%,var(--flame) 0%,var(--flame-dark) 45%),var(--flame-dark);
  overflow:hidden;
}
.flames{position:absolute;inset:155px 0 0 0;
  background:radial-gradient(ellipse at 5% 40%,#c2561a 0%,transparent 30%),
             radial-gradient(ellipse at 98% 70%,#c2561a 0%,transparent 25%),
             radial-gradient(ellipse at 50% 100%,#a3400f 0%,transparent 40%),
             var(--flame-dark);}
.header-logo{position:absolute;left:0;top:0;width:380px;height:155px;
  background:linear-gradient(180deg,#fbd08a 0%,var(--logo-orange) 55%,#c9440d 100%);
  display:flex;flex-direction:column;align-items:center;justify-content:center;gap:6px}
.brand-name{font-family:"Alfa Slab One",serif;font-size:34px;color:var(--logo-navy);letter-spacing:1px}
.brand-phone{font-family:"Arimo",Arial,sans-serif;font-weight:700;font-size:13px;color:var(--ink)}
.header-photo{position:absolute;left:380px;top:0;width:450px;height:155px;
  background:linear-gradient(90deg,#1a1210 0%,#3a231c 40%,#8c4a44 70%,#2a1a16 100%)}
.parchment{position:absolute;left:32px;top:155px;width:766px;height:1050px;
  background:radial-gradient(ellipse at 50% 45%,var(--parchment-light) 0%,var(--parchment-mid) 65%,var(--parchment-edge) 100%);
  border-radius:4px 4px 14px 10px}
.plank{position:absolute;height:46px;padding:0 16px;
  background:linear-gradient(180deg,#7a5232,var(--plank) 50%,var(--plank-dark));
  border:2px solid var(--plank-dark);box-shadow:2px 3px 4px rgba(0,0,0,.45);
  font-family:"Alfa Slab One",serif;font-size:31px;line-height:42px;color:#fff;letter-spacing:1px;
  -webkit-text-stroke:1px #2a1a0e}
.item{position:absolute;width:298px}
.item h3{font-size:14px;font-weight:700;line-height:16px}
.item h3 .price,.price{color:var(--red)}
.item h3 small{font-size:10px}
.item p{font-size:9.5px;line-height:12px;margin-top:1px}
.note{position:absolute;width:300px;font-size:11.5px;font-weight:700;line-height:15px}
.note.red{color:var(--red)}
.star{position:absolute;left:-14px;top:0}
.left{left:87px}.right{left:456px}
.tag{position:absolute;display:flex;align-items:center;gap:5px;font-size:11.5px;font-weight:700}
.tag.heart{left:265px;top:182px;color:var(--red)}
.tag.gf{left:283px;top:452px;color:var(--blue)}
.sides{position:absolute;font-size:13.5px;font-weight:700;line-height:17px}
.drink-row{position:absolute;left:456px;top:1133px;width:300px;display:flex;justify-content:space-between;font-size:13.5px;font-weight:700;text-align:center;line-height:17px}
.brand-chip{position:absolute;left:703px;width:50px;height:17px;border-radius:2px}
.loyalty{position:absolute;left:434px;top:1222px;display:flex;align-items:center;gap:12px;color:#fff;font-size:11.5px;font-weight:700;line-height:15px}
.loyalty-name{font-size:22px;font-weight:400;color:#5bb6e6}
</style>
</head>
<body>
<main class="menu">
  <div class="flames" role="img" aria-label="Dark background with glowing fire flames"></div>

  <header>
    <div class="header-logo">
      <div class="brand-name">POLLARDS BARBEQUE</div>
      <div class="brand-phone">505-555-0142</div>
    </div>
    <div class="header-photo" role="img" aria-label="Photo of a knife slicing smoked bison brisket on a board"></div>
  </header>

  <div class="parchment" role="img" aria-label="Aged parchment paper with burnt edges"></div>

  <!-- Bison -->
  <div class="plank" style="left:65px;top:178px">BISON</div>
  <div class="tag heart">
    <svg width="40" height="44" role="img" aria-label="Heart healthy mascot"><rect x="4" y="4" width="32" height="36" rx="14" fill="#f0a38c"/></svg>
    Heart Healthy
  </div>
  <div class="item left" style="top:238px"><h3>Bison Brisket - <span class="price">18.65</span></h3><p>The belly of beast,  smoked then sliced  thin and grilled. Juicy and tender</p></div>
  <div class="item left" style="top:295px"><h3>Bison Burger - <span class="price">12.59</span></h3><p>Smoked then grilled served with pepper jack cheese lettuce tomato pickle toped with spicy ranch.</p></div>
  <div class="item left" style="top:352px"><h3>Bison Steak - <span class="price">34.56</span></h3><p>12oz of lean healthy meat  cooked to your desired temp.</p></div>
  <div class="note left" style="top:393px"><span class="star">*</span>Served with 1 sides and your choice of Texas toast, Kaiser bun, or Glutton Free bread</div>

  <!-- Smoked -->
  <div class="plank" style="left:72px;top:440px">SMOKED</div>
  <div class="tag gf">
    <svg width="28" height="28"><circle cx="14" cy="14" r="13" fill="var(--blue)"/></svg>
    Glutton free
  </div>
  <div class="item left" style="top:500px;left:93px"><h3>Baby Back Ribs - <small>Full Rack <span class="price">22.59</span> - Half Rack <span class="price">12.49</span></small></h3><p>Tender to the bone, finger licking good, never need a knife, best ribs you'll ever have.</p></div>
  <div class="item left" style="top:553px;left:93px"><h3>St. Louis Ribs - <small>Half <span class="price">16.45</span> - Full <span class="price">30.89</span></small></h3><p>A nice big tender rib , slow smoked, so tender that you can sink your teeth into.</p></div>
  <div class="item left" style="top:607px;left:93px"><h3>Beef Brisket - <span class="price">10.95</span></h3><p>The most insane mouth watering smoky, moist, succulent piece of meat your mouth will ever have.</p></div>
  <div class="item left" style="top:661px;left:93px"><h3>Pulled Pork - <span class="price">9.59</span></h3><p>Smoked for 18-20 hrs. then pulled and mixed with  our signature base    barbeque sauce .</p></div>
  <div class="item left" style="top:715px;left:93px"><h3>Sliced Pork - <span class="price">10.54</span></h3><p>Smoked juicy tenderloin sliced thin then grilled per order .</p></div>
  <div class="item left" style="top:757px;left:93px"><h3>Smoked Turkey - <span class="price">11.49</span></h3><p>Breast meat smoked and sliced. Juicy and tender .</p></div>
  <div class="item left" style="top:799px;left:93px"><h3>Smoked Chicken half - <span class="price">13.59</span></h3><p>Moist and juicy smoked Breast and thigh on the bone basted with our signature sauce on the grill.</p></div>
  <div class="item left" style="top:853px;left:93px"><h3>Rib Eye - <span class="price">21.95</span></h3><p>12oz  juicy steak grilled to your desired temp</p></div>
  <div class="note" style="top:898px;left:93px"><span class="star">*</span>Served with 1 sides and your choice of Texas toast, Kaiser bun, or Glutton Free bread</div>
  <div class="note red" style="top:934px;left:93px"><span class="star" style="left:-26px">* *</span>All meats are Glutton free Please specify if you are glutton Intolerant.</div>

  <!-- Salads -->
  <div class="plank" style="left:66px;top:987px">SALADS</div>
  <div class="item left" style="top:1049px"><h3>All you can eat salad bar - <span class="price">7.89</span></h3><p>Enjoy as much salad as you would like</p></div>
  <div class="item left" style="top:1096px"><h3>Meaty Salad - <span class="price">3.00</span></h3><p>Choose any meat to  add to your salad  3oz of meat .<br>(Excludes ribs and bison.)</p></div>
  <div class="item left" style="top:1150px;width:320px"><h3>Side Salad - <small>With out meal <span class="price">3.00</span> - Add to meal <span class="price">1.50</span></small></h3></div>

  <!-- Appetizers -->
  <div class="plank" style="left:435px;top:180px">APPETIZERS</div>
  <div class="item right" style="top:242px"><h3>King Rings - <span class="price">7.89</span></h3><p>Green Chili battered  fried golden crispy 1" thick    onion rings. Served with spicy ranch.</p></div>
  <div class="item right" style="top:296px"><h3>Deep Fried Pickles - <span class="price">7.89</span></h3><p>Crisp dill pickle chips battered and fried to a golden   crispy brown. Served with spicy ranch.</p></div>
  <div class="item right" style="top:350px"><h3>Fried Okra - <span class="price">7.89</span></h3><p>Okra  is breaded then fried until golden. Served with spicy ranch.</p></div>
  <div class="item right" style="top:392px"><h3>Green Chili Waffle Fries - <span class="price">7.89</span></h3><p>Crispy waffle-cut Fries, topped with a savory blend of cheese, and New Mexico green  chile. Served with spicy ranch.</p></div>
  <div class="item right" style="top:446px"><h3>KC Wild Wings - <span class="price">9.99</span></h3><p>Big, meaty pork wings,  deep fried to a perfect    golden brown, tossed in a hot Buffalo-style sauce, and served with spicy buttermilk ranch dressing on the side. Served with spicy ranch.</p></div>
  <div class="item right" style="top:517px"><h3>Sampler Platter - <span class="price">8.99</span></h3><p>Two KC Wild Wings, 6oz of Fried Pickles, 6oz of King Rings. Served with spicy ranch.</p></div>

  <!-- Sides -->
  <div class="plank" style="left:435px;top:578px">SIDES</div>
  <div class="sides" style="left:456px;top:640px">*Green Chile Creamed Corn<br>*Potato Salad<br>*Baked Potato<br>*Grilled Veggies</div>
  <div class="sides" style="left:661px;top:657px">*Baked Beans<br>*Waffle Fries<br>*Coleslaw</div>
  <div class="sides" style="left:456px;top:726px;color:var(--red);font-size:13px">**Extra side 2.29</div>

  <!-- Desserts -->
  <div class="plank" style="left:435px;top:757px">DESSERTS</div>
  <div class="item right" style="top:820px;width:310px"><h3>Peach Cobbler <span class="price">&amp;</span> Ice Cream - <small>large <span class="price">5.89</span> Small <span class="price">3.29</span></small></h3><p>Served hot topped with ice cream.</p></div>
  <div class="item right" style="top:866px"><h3>Cookies A-L-Mode - <small>large <span class="price">5.89</span> Small <span class="price">3.29</span></small></h3><p>Hot gooey cookies topped with ice cream your choice chocolate chip or macadamia nut.  large 5.89 Small</p></div>
  <div class="note right" style="top:924px;font-size:11.5px"><span class="star">*</span>Dessert of the week<br><span class="price">Ask your server for our special dessert of the week</span></div>

  <!-- Drinks -->
  <div class="plank" style="left:435px;top:972px">DRINKS</div>
  <div class="brand-chip" style="top:1031px;background:#1d4fa0"></div>
  <div class="brand-chip" style="top:1058px;background:#8b1a22"></div>
  <div class="item right" style="top:1032px;width:240px"><h3>Lemonade - <span class="price">2.59</span></h3><p>Regular, Strawberry, Watermelon, Cherry, Peach</p></div>
  <div class="item right" style="top:1074px"><h3>Fountain  - <span class="price">1.89</span></h3><p>Fizz Cola,  Doc Spice , Root Beer ,  Lemon Lift, Mtn Zing , Diet Fizz Diet Doc Spice</p></div>
  <div class="drink-row">
    <div>Iced Teas<br><span class="price">1.89</span></div>
    <div>Coffee<br><span class="price">2.69</span></div>
    <div>Hot Chocolate<br><span class="price">2.89</span></div>
  </div>

  <footer class="loyalty">
    <span class="loyalty-name">Loyalto</span>
    <span>Join our Customer loyalty app.<br>Get free food when you become a loyal customer.</span>
  </footer>
</main>
</body>
</html>
```